Bravel Acres Business Cards

design business cards for our new business should match my Corvane Quotations business cards

Contact Information for Business Card

2817 W 68th N St
Tulsa, OK 74592

Requirements
Must have
• should match logo colors

```html
<!DOCTYPE html>
<html lang="en">
<head>
<meta charset="UTF-8">
<title>Bravel Acres Business Cards</title>
<link href="https://fonts.googleapis.com/css2?family=Lato:wght@400;700;900&display=swap" rel="stylesheet">
<style>
  :root {
    --backdrop: #3a322e;
    --card: #0d2b31;
    --card-deep: #0a2329;
    --green: #6cc04a;
    --teal: #1eb3a6;
    --white: #f3f6f5;
    --rule: #1f8f86;
  }
  * { box-sizing: border-box; margin: 0; padding: 0; }
  html, body {
    width: 1200px; height: 847px; overflow: hidden;
    background: var(--backdrop);
    font-family: "Lato", sans-serif;
  }
  .stage {
    position: relative; width: 1200px; height: 847px;
    display: flex; align-items: center; justify-content: center; gap: 44px;
  }
  .card {
    position: relative; width: 540px; height: 310px;
    background: var(--card);
    box-shadow: 6px 6px 0 -1px var(--teal), 0 18px 30px rgba(0,0,0,.45);
    border-right: 3px solid var(--green);
    border-bottom: 3px solid var(--green);
    overflow: hidden;
  }
  /* back side */
  .card-back .pattern-field {
    position: absolute; inset: 0;
    background: linear-gradient(160deg, #123a40 0%, var(--card) 45%, var(--card-deep) 100%);
  }
  .card-back .back-mark {
    position: absolute; left: 50%; bottom: 46px; transform: translateX(-50%);
    font-weight: 900; font-size: 22px; color: var(--green); letter-spacing: .5px;
    white-space: nowrap;
  }
  /* front side */
  .person {
    position: absolute; left: 34px; top: 64px;
  }
  .person .name {
    font-weight: 900; font-size: 26px; color: var(--green); letter-spacing: .3px;
  }
  .person .role {
    font-size: 15px; color: var(--white); margin-top: 2px;
  }
  .divider {
    position: absolute; left: 34px; right: 34px; top: 134px;
    height: 1px; background: linear-gradient(90deg, var(--green), var(--rule));
  }
  .contacts {
    position: absolute; left: 34px; top: 152px; list-style: none;
  }
  .contacts li {
    display: flex; align-items: center; gap: 10px;
    font-size: 15px; color: var(--white); line-height: 25px;
  }
  .contacts svg { width: 13px; height: 13px; flex: none; }
  .brand {
    position: absolute; right: 40px; top: 62px;
    display: flex; align-items: center; gap: 10px;
    font-weight: 900; font-size: 34px; color: var(--green); white-space: nowrap;
  }
  .brand .dot {
    width: 14px; height: 14px; border-radius: 50%; background: var(--teal);
  }
  .address {
    position: absolute; right: 36px; bottom: 30px; text-align: right;
    font-size: 16px; color: var(--white); line-height: 24px;
  }
</style>
</head>
<body>
<main class="stage">
  <section class="card card-back" aria-label="Card back">
    <div class="pattern-field" role="img" aria-label="Faint repeating brand pattern on dark teal"></div>
    <div class="back-mark">Bravel Acres</div>
  </section>

  <section class="card card-front" aria-label="Card front">
    <div class="person">
      <div class="name">DORIAN HALVEY</div>
      <div class="role">Founder &amp; CEO</div>
    </div>
    <div class="brand"><span class="dot"></span>Bravel Acres</div>
    <div class="divider"></div>
    <ul class="contacts">
      <li>
        <svg viewBox="0 0 16 16"><path fill="#6cc04a" d="M3.6 1.5l2.3 2.6-1.3 1.7c.9 2 2.6 3.7 4.6 4.6l1.7-1.3 2.6 2.3-1.4 2.2C7 13.2 2.8 9 2.4 3z"/></svg>
        9185550147
      </li>
      <li>
        <svg viewBox="0 0 16 16"><rect x="1" y="3" width="14" height="10" fill="#6cc04a"/><path d="M1 3l7 6 7-6" fill="none" stroke="#0d2b31" stroke-width="1.4"/></svg>
        hello@bravelacres.com
      </li>
      <li>
        <svg viewBox="0 0 16 16"><g fill="none" stroke="#1eb3a6" stroke-width="1.3"><circle cx="8" cy="8" r="6.5"/><ellipse cx="8" cy="8" rx="3" ry="6.5"/><path d="M1.5 8h13"/></g></svg>
        www.bravelacres.com
      </li>
    </ul>
    <address class="address" style="font-style:normal">
      2817 W 68th N St<br>Tulsa, OK 74592
    </address>
  </section>
</main>
</body>
</html>
```